Webdesign für Honigmanufaktur
Zielgruppe
Imkerei, Verkauf von Honig und Honigerzeugnissen, so wie Bienenwachskerzen.
Zielgruppe sind vermutlich Frauen im mittleren bis gehobenen Alter.
Aufgabenstellung
Es gibt ein Firmenlogo.
Ich bevorzuge als Grundfarbe weiß, lasse mich aber von guten Einfällen gerne überraschen.
Die Website www.velmique.at finde ich sehr ansprechend.
Nur ohne Musik.
Ohne Deutsch/Englisch Auswahl.
Es soll danach Word press verwendet werden.

```html
<!DOCTYPE html>
<html lang="de">
<head>
<meta charset="utf-8">
<title>Honighaus Lindental</title>
<link href="https://fonts.googleapis.com/css2?family=Encode+Sans+Compressed:wght@300;400;700&display=swap" rel="stylesheet">
<style>
  :root {
    --bg: #ffffff;
    --text: #2b2b2b;
    --text-active: #111111;
    --brand: #5a3316;
    --amber: #e5a53a;
    --cart-bg: #58585a;
    --white: #ffffff;
    --olive-dark: #4f4b1c;
    --olive: #7d7424;
    --gold-deep: #9a6a10;
    --gold: #c99a1e;
    --gold-bright: #e2b42e;
    --seed-brown: #6e4a0c;
  }
  * { margin: 0; padding: 0; box-sizing: border-box; }
  html, body {
    width: 1200px; height: 700px; overflow: hidden;
    background: var(--bg);
    font-family: "Encode Sans Compressed", "Arial Narrow", sans-serif;
  }
  .page { position: relative; width: 1200px; height: 700px; }

  .site-header { position: absolute; top: 0; left: 0; width: 1200px; height: 125px; background: var(--bg); }
  .nav-link {
    position: absolute; top: 50px;
    font-size: 26px; font-weight: 300; color: var(--text);
    text-decoration: none; line-height: 1;
  }
  .nav-link.is-active { color: var(--text-active); font-weight: 400; }
  .nav-link.is-active::after {
    content: ""; position: absolute; left: -9px; right: -5px; top: 33px;
    height: 2px; background: var(--text-active);
  }

  .brand {
    position: absolute; left: 521px; top: 10px; width: 160px;
    text-align: center; color: var(--brand);
  }
  .brand-mark {
    display: block; width: 54px; height: 54px; margin: 0 auto 12px;
    border-radius: 50%; background: var(--amber);
  }
  .brand-name {
    font-size: 16px; font-weight: 700; letter-spacing: 0.6px; line-height: 1;
  }

  .cart-button {
    position: absolute; left: 1150px; top: 36px; width: 50px; height: 53px;
    background: var(--cart-bg); display: flex; align-items: center; justify-content: center;
  }

  .hero {
    position: absolute; top: 125px; left: 0; width: 1200px; height: 575px;
    background:
      radial-gradient(ellipse 180px 140px at 620px 420px, rgba(60,45,20,0.45) 0%, transparent 100%),
      radial-gradient(ellipse 420px 380px at 1020px 260px, rgba(110,74,12,0.55) 0%, transparent 100%),
      radial-gradient(ellipse 260px 300px at 760px 300px, rgba(238,190,50,0.7) 0%, transparent 100%),
      radial-gradient(ellipse 300px 240px at 80px 540px, rgba(226,180,46,0.85) 0%, transparent 100%),
      radial-gradient(ellipse 360px 200px at 300px 60px, rgba(110,118,40,0.6) 0%, transparent 100%),
      radial-gradient(ellipse 260px 260px at 60px 160px, rgba(79,75,28,0.8) 0%, transparent 100%),
      linear-gradient(100deg, var(--olive) 0%, var(--gold) 38%, var(--gold-bright) 58%, var(--gold-deep) 82%, var(--seed-brown) 100%);
  }
  .hero-title {
    position: absolute; left: 107px; top: 165px;
    font-size: 46px; font-weight: 400; color: var(--white); line-height: 1;
  }
  .hero-arrow { position: absolute; }
  .hero-arrow.prev { left: 20px; top: 242px; }
  .hero-arrow.next { left: 1140px; top: 248px; }
</style>
</head>
<body>
<div class="page">
  <header class="site-header">
    <a class="nav-link is-active" style="left:88px" href="#">Manufaktur</a>
    <a class="nav-link" style="left:238px" href="#">Bienen</a>
    <a class="nav-link" style="left:350px" href="#">Bienenwachs</a>
    <div class="brand">
      <span class="brand-mark"></span>
      <div class="brand-name">HONIGHAUS LINDENTAL</div>
    </div>
    <a class="nav-link" style="left:757px" href="#">Shop</a>
    <a class="nav-link" style="left:864px" href="#">Kontakt</a>
    <a class="cart-button" href="#" aria-label="Warenkorb">
      <svg width="22" height="20" viewBox="0 0 22 20" fill="none" stroke="#fff" stroke-width="1.8" stroke-linejoin="round" stroke-linecap="round">
        <path d="M1 2h3l3 11h11l2-8H5.5"/>
        <path d="M9 6v6M13 6v6M17 6v6"/>
        <circle cx="8.5" cy="17" r="1.5"/><circle cx="16.5" cy="17" r="1.5"/>
      </svg>
    </a>
  </header>
  <section class="hero" role="img" aria-label="Nahaufnahme einer Biene, die auf einer Sonnenblume Pollen sammelt">
    <h1 class="hero-title">Einzigartiger Honig</h1>
    <svg class="hero-arrow prev" width="36" height="74" viewBox="0 0 36 74" fill="none" stroke="#fff" stroke-width="1.5">
      <path d="M34 1L2 37l32 36"/>
    </svg>
    <svg class="hero-arrow next" width="50" height="76" viewBox="0 0 50 76" fill="none" stroke="#fff" stroke-width="1.5">
      <path d="M2 1l46 37L2 75"/>
    </svg>
  </section>
</div>
</body>
</html>
```